Night Dresses business cards business requirers

We are a new company initiating Mexico operations. Our core business is Night woman dress (both formal and party dress) for rent. Gownhaven is the name of the company. ITS Gownhaven form by two word. The dress word and topia (Utopic) so the place Gownhaven Means That You cant get the ideal, perfect and unique dress for your event. So we would like a modern, very creative, and attractive business card.

Industry/Entity Type

Womens Clothing

Contact Information for Business Card

Rounded Borders, two faces

Requirements
Must have
• Rounded borders, logo and slogan, modern, glam, attractive design
Should not have
• modern design classic or not

```html
<!DOCTYPE html>
<html lang="en">
<head>
<meta charset="utf-8">
<title>Gownhaven Business Card</title>
<link rel="stylesheet" href="https://fonts.googleapis.com/css2?family=Montserrat:wght@400;500&family=Oranienbaum&display=swap">
<style>
  :root {
    --page: #ffffff;
    --rose-dark: #b2587f;
    --rose: #d77aa1;
    --rose-light: #e6a3c0;
    --gold-dark: #d9a91c;
    --gold: #f2d34a;
    --gold-light: #fbe97a;
    --satin: #f4f2f0;
    --satin-shade: #e6e3e0;
    --ink: #111111;
    --accent: #b65a8c;
  }
  * { margin: 0; padding: 0; box-sizing: border-box; }
  html, body {
    width: 1200px; height: 720px; overflow: hidden;
    background: var(--page);
  }
  .canvas { position: relative; width: 1200px; height: 720px; }
  .card {
    position: absolute; left: 44px; top: 43px;
    width: 1113px; height: 630px;
    border-radius: 52px; overflow: hidden;
  }
  .satin-rose {
    position: absolute; inset: 0;
    background: linear-gradient(115deg, var(--rose-dark) 0%, var(--rose) 35%, var(--rose-light) 55%, var(--rose) 75%, var(--rose-dark) 100%);
  }
  .gold-band {
    position: absolute; left: 0; width: 100%; height: 42px;
    background: linear-gradient(90deg, var(--gold-dark) 0%, var(--gold) 25%, var(--gold-light) 50%, var(--gold) 70%, var(--gold-dark) 100%);
  }
  .gold-band--top { top: 63px; }
  .gold-band--bottom { top: 525px; }
  .satin-white {
    position: absolute; left: 0; top: 105px; width: 100%; height: 420px;
    background: linear-gradient(120deg, var(--satin) 0%, var(--satin-shade) 30%, var(--satin) 50%, var(--satin-shade) 75%, var(--satin) 100%);
  }
  .brand {
    position: absolute; left: 42px; top: 138px;
    display: flex; align-items: center; gap: 14px;
  }
  .brand-mark {
    width: 34px; height: 34px; background: var(--accent);
  }
  .brand-text { display: flex; flex-direction: column; align-items: flex-start; }
  .brand-name {
    font-family: "Montserrat", sans-serif; font-weight: 500;
    font-size: 24px; line-height: 26px; color: var(--ink);
  }
  .brand-slogan {
    font-family: "Montserrat", sans-serif; font-weight: 400;
    font-size: 13px; line-height: 16px; color: var(--ink);
    margin-top: 2px;
  }
  .rule {
    position: absolute; top: 279px; height: 2px; background: var(--ink);
  }
  .rule--left { left: 0; width: 331px; }
  .rule--right { left: 779px; width: 334px; }
  .identity {
    position: absolute; left: 331px; width: 448px; top: 226px;
    text-align: center;
  }
  .person-name {
    font-family: "Oranienbaum", serif; font-weight: 400;
    font-size: 80px; line-height: 80px; color: var(--ink);
    white-space: nowrap;
    transform: scaleX(0.6); transform-origin: center;
    margin: 0 -200px;
  }
  .person-role {
    font-family: "Montserrat", sans-serif; font-weight: 400;
    font-size: 22px; line-height: 26px; letter-spacing: 6px; color: var(--ink);
    margin-top: 8px; word-spacing: 14px; white-space: nowrap;
  }
  .contacts {
    position: absolute; left: 0; top: 457px; width: 100%; height: 40px;
    font-family: "Montserrat", sans-serif; font-size: 21px; color: var(--ink);
  }
  .contact { position: absolute; top: 0; display: flex; align-items: center; gap: 8px; height: 40px; white-space: nowrap; }
  .contact--phone { left: 46px; }
  .contact--address { left: 291px; }
  .contact--email { left: 731px; gap: 11px; }
  .contact svg { stroke: var(--accent); fill: none; stroke-width: 2; }
</style>
</head>
<body>
<div class="canvas">
  <div class="card">
    <div class="satin-rose" role="img" aria-label="Rose pink draped satin fabric"></div>
    <div class="gold-band gold-band--top"></div>
    <div class="satin-white" role="img" aria-label="White draped satin fabric"></div>
    <div class="gold-band gold-band--bottom"></div>

    <div class="brand">
      <div class="brand-mark"></div>
      <div class="brand-text">
        <span class="brand-name">Gownhaven</span>
        <span class="brand-slogan">Evening gowns to rent</span>
      </div>
    </div>

    <div class="rule rule--left"></div>
    <div class="rule rule--right"></div>
    <div class="identity">
      <div class="person-name">YOUR NAME HERE</div>
      <div class="person-role">YOUR POSITION</div>
    </div>

    <div class="contacts">
      <div class="contact contact--phone">
        <svg width="38" height="38" viewBox="0 0 24 24" aria-hidden="true">
          <path d="M5 3h3l2 5-2.5 1.5a11 11 0 0 0 6 6L15 13l5 2v3a2 2 0 0 1-2 2A16 16 0 0 1 3 5a2 2 0 0 1 2-2z" stroke-width="1.2"/>
        </svg>
        <span>(123) 456 7890</span>
      </div>
      <div class="contact contact--address">
        <svg width="30" height="42" viewBox="0 0 20 28" aria-hidden="true">
          <path d="M10 27C10 27 2 16 2 10a8 8 0 0 1 16 0c0 6-8 17-8 17z" stroke-width="1.4"/>
          <circle cx="10" cy="10" r="3.5" stroke-width="1.4"/>
        </svg>
        <span>123 N. STREET, CITY, STATE 12345</span>
      </div>
      <div class="contact contact--email">
        <svg width="46" height="34" viewBox="0 0 46 34" aria-hidden="true">
          <rect x="1" y="1" width="44" height="32" stroke-width="1.6"/>
          <path d="M1 1l22 18L45 1M1 33l16-16M45 33L29 17" stroke-width="1.6"/>
        </svg>
        <span>NAME@COMPANY.COM</span>
      </div>
    </div>
  </div>
</div>
</body>
</html>
```